Home Improvements Website

I would like a website that matches our business colour scheme and uses the fonts consistent without logo. (Monserrat, Chosence & Big Noddle Tiling).
We will need numerous sections: homepage, about us, services (with tiles or links to each service - building, landscaping, decking, maintenance, roofing, gutters etc) current projects (which must be easily editable by me, who is not too tech savvy) and a contacts page with enquiry form we can link to our job management service (Tradify).

```html
<!DOCTYPE html>
<html lang="en">
<head>
<meta charset="utf-8">
<title>Halvard Home Improvements</title>
<link href="https://fonts.googleapis.com/css2?family=Bebas+Neue&family=Montserrat:wght@400;500;600;700&display=swap" rel="stylesheet">
<style>
:root{
  --gold:#b08f4f;
  --dark:#2f3532;
  --footer:#363b38;
  --light:#f0f0f0;
  --field:#eeeeee;
  --text:#444;
  --white:#fff;
  --star:#e8b631;
}
*{margin:0;padding:0;box-sizing:border-box}
html,body{width:1200px;height:5372px;overflow:hidden}
body{position:relative;font-family:"Montserrat",sans-serif;color:var(--text);background:var(--white)}
.abs{position:absolute}
.display{font-family:"Bebas Neue",sans-serif;letter-spacing:.5px;color:var(--dark);font-weight:400}
.ph{position:absolute}

/* header */
.site-header{left:0;top:0;width:1200px;height:90px;background:var(--white);z-index:5}
.brand{left:95px;top:10px;width:104px;height:124px;background:var(--white);display:flex;flex-direction:column;align-items:center;justify-content:center;gap:6px;z-index:6}
.brand-dot{width:18px;height:18px;border-radius:50%;background:var(--gold)}
.brand-name{font-family:"Montserrat",sans-serif;font-weight:700;font-size:14px;color:var(--dark);letter-spacing:1px}
.nav{left:353px;top:36px;display:flex;gap:30px;font-size:12px;font-weight:500;color:var(--dark)}
.btn-quote{left:947px;top:24px;width:163px;height:42px;background:var(--dark);color:#fff;font-size:12px;font-weight:700;display:flex;align-items:center;justify-content:center}

/* hero */
.hero-photo{left:0;top:90px;width:1200px;height:1100px;background:linear-gradient(160deg,#c8ccd2 0%,#9aa0a8 35%,#6b5a44 60%,#4a4e52 100%)}
.hero-title{left:88px;top:222px;font-size:88px;line-height:80px;color:#fff}
.hero-sub{left:88px;top:404px;font-size:17px;color:#fff}
.hero-line{left:124px;top:450px;width:1px;height:150px;background:rgba(255,255,255,.6)}
.mouse{left:113px;top:628px;width:22px;height:34px;border:2px solid #fff;border-radius:11px}
.mouse::after{content:"";position:absolute;left:8px;top:6px;width:2px;height:7px;background:#fff}
.gold-shape{left:0;top:0}
.about-vert{left:120px;top:1120px;transform:rotate(-90deg);transform-origin:left top;font-size:38px;color:#fff;white-space:nowrap}
.about-head{left:223px;top:922px;font-size:22px;color:#fff}
.about-text{left:223px;top:960px;width:390px;font-size:13px;line-height:20px;color:#fff}
.about-rule{left:223px;top:1060px;width:392px;height:1px;background:rgba(255,255,255,.5)}
.avatar{width:72px;height:72px;border-radius:50%;background:#8a7a6a;border:4px solid #fff}
.owner{left:306px;top:1094px;color:#fff}
.owner b{display:block;font-family:"Bebas Neue",sans-serif;font-weight:400;font-size:22px}
.owner span{font-family:"Bebas Neue",sans-serif;font-size:13px}

.inspect-form{left:741px;top:710px;width:409px;height:521px;background:#fff;box-shadow:0 10px 40px rgba(0,0,0,.15);padding:30px 32px}
.inspect-form h3{font-size:24px;margin-bottom:22px}
.lbl{font-family:"Bebas Neue",sans-serif;font-size:13px;color:var(--dark);display:block;margin-bottom:6px}
.field{height:42px;background:var(--field);font-size:11px;color:#999;display:flex;align-items:center;justify-content:space-between;padding:0 20px;margin-bottom:18px}
.row{display:flex;gap:10px}.row>div{flex:1}
.btn-submit{height:42px;background:var(--dark);color:#fff;font-size:13px;font-weight:700;display:flex;align-items:center;justify-content:center;position:relative;margin-top:12px}

/* sections */
.sec-title{width:1200px;left:0;text-align:center;font-size:36px}
.sec-sub{width:1200px;left:0;text-align:center;font-size:14px;color:var(--text)}
.video{left:181px;top:1569px;width:838px;height:460px;background:linear-gradient(180deg,#c9d6e0 0%,#8c8d95 45%,#5c7a3a 80%,#4d6b2e 100%);box-shadow:0 20px 40px rgba(0,0,0,.15)}
.play{left:556px;top:1755px;width:88px;height:88px;border-radius:50%;background:rgba(40,40,40,.55)}

.tile{top:2243px;height:376px}
.tile-bar{position:absolute;left:24px;right:24px;bottom:28px;height:66px;background:rgba(255,255,255,.9);display:flex;align-items:center;justify-content:space-between;padding:0 24px;font-family:"Bebas Neue",sans-serif;font-size:24px;color:var(--dark)}
.arrow-btn{width:50px;height:50px;border-radius:50%;display:flex;align-items:center;justify-content:center}
.arrow-btn.gold{background:var(--gold)}.arrow-btn.dark{background:var(--dark)}

.stats{left:0;top:2790px;width:1200px;height:192px;background:var(--light)}
.stat{top:2846px;border-left:4px solid var(--gold);padding-left:20px;height:76px}
.stat b{display:block;font-family:"Bebas Neue",sans-serif;font-weight:400;font-size:54px;line-height:50px;color:var(--dark)}
.stat span{font-family:"Bebas Neue",sans-serif;font-size:16px;color:var(--dark)}

.project{width:297px;height:297px}
.btn-dark{background:var(--dark);color:#fff;font-size:12px;font-weight:700;display:flex;align-items:center;justify-content:center}

.review{text-align:left;padding:0 0}
.review p{font-size:12.5px;line-height:21px;color:#555}
.review .who{margin-top:20px;font-family:"Bebas Neue",sans-serif;font-size:17px;color:var(--dark);display:flex;gap:10px;align-items:center}
.stars{color:var(--star);font-size:13px;letter-spacing:1px}

/* offer */
.offer{left:115px;top:4418px;width:970px;height:478px;background:var(--field);overflow:hidden}
.offer-photo{left:0;top:200px;width:970px;height:278px;background:linear-gradient(170deg,#b9bcbe 0%,#7f8386 60%,#5f6366 100%);clip-path:polygon(0 12%,100% 0,100% 100%,0 100%)}
.quote-card{left:223px;top:4477px;width:336px;height:359px;background:#fff;padding:28px 30px}
.qf{height:32px;background:var(--field);font-family:"Bebas Neue",sans-serif;font-size:13px;color:var(--dark);display:flex;align-items:center;justify-content:space-between;padding:0 12px;margin-bottom:10px}
.toggle{left:674px;top:4680px;width:110px;height:48px;border-radius:24px;background:#fff}

/* footer */
.footer{left:0;top:4760px;width:1200px;height:612px;background:var(--footer);z-index:-1}
.f-head{font-family:"Bebas Neue",sans-serif;font-size:24px;color:#fff}
.f-list{font-size:12px;line-height:22px;color:#c9c9c9}
.contact-item{display:flex;gap:12px;font-size:12px;line-height:16px;color:#c9c9c9;margin-bottom:14px}
.strip{left:0;top:5243px;width:1200px;height:50px;border-top:1px solid #4c514e;border-bottom:1px solid #4c514e;display:flex}
.strip div{flex:1;display:flex;align-items:center;justify-content:center;font-size:11px;color:#ddd;border-right:1px solid #4c514e}
.strip div:last-child{border-right:none}
.social{width:28px;height:28px;border-radius:50%;background:#4a4f4c}
</style>
</head>
<body>

<header class="abs site-header">
  <nav class="abs nav"><span>HOME</span><span>ABOUT US</span><span>SERVICES ▾</span><span>PROJECTS</span><span>LATEST BLOG</span><span>CONTACT US</span></nav>
  <div class="abs btn-quote">GET A FREE QUOTE</div>
</header>
<div class="abs brand"><span class="brand-dot"></span><span class="brand-name">HALVARD</span></div>

<section>
  <div class="ph hero-photo" role="img" aria-label="Timber-clad house gable with dark metal roof under a cloudy sky"></div>
  <h1 class="abs display hero-title">HALVARD HOME<br>IMPROVEMENTS</h1>
  <p class="abs display hero-sub">IS YOUR SOURCE FOR ROOFING AND SIDING IN MINNESOTA.</p>
  <div class="abs hero-line"></div>
  <div class="abs mouse"></div>
  <svg class="abs gold-shape" width="1200" height="1400" viewBox="0 0 1200 1400">
    <polygon points="0,678 595,897 1200,689 1200,1127 595,1357 0,1127" fill="#b08f4f"/>
    <polygon points="1200,1127 1200,1190 595,1400 595,1357" fill="#ffffff"/>
  </svg>
  <div class="abs display about-vert">ABOUT HALVARD</div>
  <h2 class="abs display about-head">HALVARD HOME IMPROVEMENTS</h2>
  <p class="abs about-text">You deserve timely service, high quality materials, expert installation, and an ironclad warranty. That is what we promise to deliver. I invite you to put us to the test today. Sincerely,</p>
  <div class="abs about-rule"></div>
  <div class="abs avatar" role="img" aria-label="Portrait of the owner" style="left:223px;top:1082px"></div>
  <div class="abs owner"><b>LEO BRANDT, OWNER</b><span>HALVARD CONSTRUCTION</span></div>

  <form class="abs inspect-form">
    <h3 class="display">SAME DAY INSPECTIONS AVAILABLE</h3>
    <span class="lbl">NAME*</span><div class="field">Enter your name</div>
    <div class="row">
      <div><span class="lbl">PHONE*</span><div class="field">Enter number</div></div>
      <div><span class="lbl">ZIP CODE*</span><div class="field">Select <span>⌄</span></div></div>
    </div>
    <span class="lbl">EMAIL*</span><div class="field">Enter email</div>
    <span class="lbl">MESSAGE*</span><div class="field" style="height:100px;align-items:flex-start;padding-top:14px">Type your message</div>
    <div class="btn-submit">SUBMIT
      <svg style="position:absolute;right:22px" width="14" height="14" viewBox="0 0 24 24"><path d="M2 12 22 3 15 22 11 13Z" fill="#fff"/></svg></div>
  </form>
</section>

<section>
  <h2 class="abs display sec-title" style="top:1418px">WATCH OUR HIGHLIGHTS</h2>
  <p class="abs sec-sub" style="top:1474px">In 2016 Leo Brandt started helping people with their home improvement projects.</p>
  <div class="ph video" role="img" aria-label="Two-storey stone and siding family home with a green lawn"></div>
  <div class="abs play"><svg width="88" height="88" viewBox="0 0 88 88"><path d="M38 34 54 44 38 54Z" fill="#fff"/></svg></div>
</section>

<section>
  <h2 class="abs display sec-title" style="top:2132px">OUR SERVICES</h2>
  <p class="abs sec-sub" style="top:2186px">What we do: building, landscaping, decking, maintenance, roofing, gutter...</p>
  <div class="abs tile" role="img" aria-label="Landscapers laying a garden path" style="left:0;width:271px;background:linear-gradient(160deg,#6f8f4a,#3d5a2a)"><div class="tile-bar">LANDSCAPING <span>→</span></div></div>
  <div class="abs tile" role="img" aria-label="Timber deck with outdoor furniture" style="left:290px;width:296px;background:linear-gradient(170deg,#8fa6b8,#7a5236)"><div class="tile-bar">DECKING <span>→</span></div></div>
  <div class="abs tile" role="img" aria-label="Roofer working on tiles" style="left:605px;width:297px;background:linear-gradient(170deg,#8fa8c8,#5a5f66,#b07a4a)"><div class="tile-bar">ROOFING <span>→</span></div></div>
  <div class="abs tile" role="img" aria-label="Glass office building" style="left:920px;width:280px;background:linear-gradient(160deg,#b6cbdc,#3e6a86)"><div class="tile-bar">BUILDING <span>→</span></div></div>
  <div class="abs arrow-btn gold" style="left:545px;top:2673px"><svg width="16" height="16" viewBox="0 0 24 24"><path d="M20 12H4M10 6 4 12l6 6" stroke="#fff" stroke-width="2" fill="none"/></svg></div>
  <div class="abs arrow-btn dark" style="left:601px;top:2673px"><svg width="16" height="16" viewBox="0 0 24 24"><path d="M4 12h16M14 6l6 6-6 6" stroke="#fff" stroke-width="2" fill="none"/></svg></div>
</section>

<section class="abs stats">
</section>
<div class="abs stat" style="left:265px"><b>800</b><span>TOTAL PROJECTS</span></div>
<div class="abs stat" style="left:501px"><b>20M</b><span>REVENUE EARNED ALL TIME</span></div>
<div class="abs stat" style="left:795px"><b>500</b><span>CLIENT'S FEEDBACK</span></div>

<section>
  <h2 class="abs display sec-title" style="top:3050px">CURRENT PROJECTS</h2>
  <div class="abs project" role="img" aria-label="Deck chairs on a balcony overlooking the sea" style="left:131px;top:3122px;background:linear-gradient(170deg,#c9d3da,#7a5a3e)"></div>
  <div class="abs project" role="img" aria-label="Roofer installing shingles" style="left:451px;top:3122px;background:linear-gradient(170deg,#9a9da0,#c9a67a)"></div>
  <div class="abs project" role="img" aria-label="Gardener planting shrubs" style="left:768px;top:3122px;background:linear-gradient(170deg,#7a9a5a,#c85a2a,#4d6b2e)"></div>
  <div class="abs project" role="img" aria-label="Worker fixing roof panels" style="left:131px;top:3439px;background:linear-gradient(160deg,#a9c4dc,#7a6a5a)"></div>
  <div class="abs project" role="img" aria-label="House with timber siding and grey roof" style="left:451px;top:3439px;background:linear-gradient(170deg,#a9c4dc,#4a4e52,#8a5a36)"></div>
  <div class="abs project" role="img" aria-label="Curved modern building facade" style="left:768px;top:3439px;background:linear-gradient(160deg,#2a2a2a,#9a9a9a,#3a3a3a)"></div>
  <div class="abs btn-dark" style="left:495px;top:3788px;width:206px;height:46px">VIEW ALL PROJECTS</div>
</section>

<section>
  <h2 class="abs display sec-title" style="top:3923px">WHAT OUR CLIENTS SAY ABOUT US</h2>
  <div class="abs" style="left:432px;top:3997px;width:330px;height:250px;background:var(--light)"></div>
  <div class="abs avatar" role="img" aria-label="Client portrait" style="left:124px;top:3992px;border:none"></div>
  <div class="abs avatar" role="img" aria-label="Client portrait" style="left:471px;top:3992px;border:none"></div>
  <div class="abs avatar" role="img" aria-label="Client portrait" style="left:815px;top:3992px;border:none"></div>
  <div class="abs review" style="left:115px;top:4100px;width:282px"><p>I never dreamed my roof would look this good. I thought I had to replace it. Thank you Ridgeline for saving me thousands of dollars.</p><div class="who">OWEN P. <span class="stars">★★★★★</span></div></div>
  <div class="abs review" style="left:463px;top:4100px;width:280px"><p>Can't believe how sturdy this stuff makes roofing shingles. You have to see it to believe it. Plus, they look great, too! Just like new.</p><div class="who">MARK D. <span class="stars">★★★★★</span></div></div>
  <div class="abs review" style="left:808px;top:4100px;width:280px"><p>I am now a believer in the Ridgeline product. Our roof is 42 years old, we couldn't afford a new roof. It is amazing the transformation for our roof.</p><div class="who">ETHAN K. <span class="stars">★★★★★</span></div></div>
  <div class="abs arrow-btn gold" style="left:545px;top:4287px"><svg width="16" height="16" viewBox="0 0 24 24"><path d="M20 12H4M10 6 4 12l6 6" stroke="#fff" stroke-width="2" fill="none"/></svg></div>
  <div class="abs arrow-btn dark" style="left:601px;top:4287px"><svg width="16" height="16" viewBox="0 0 24 24"><path d="M4 12h16M14 6l6 6-6 6" stroke="#fff" stroke-width="2" fill="none"/></svg></div>
</section>

<div class="abs footer"></div>

<section>
  <div class="abs offer">
    <div class="ph offer-photo" role="img" aria-label="Grey asphalt shingle roof"></div>
  </div>
  <form class="abs quote-card">
    <div class="qf">FULL NAME</div>
    <div class="row"><div class="qf">EMAIL</div><div class="qf">PHONE <span>⌄</span></div></div>
    <div class="qf">ADDRESS</div>
    <div class="row"><div class="qf">CITY</div><div class="qf">STATE</div></div>
    <div class="qf">PROJECT</div>
    <div class="qf">I AM A <span>⌄</span></div>
    <div class="btn-dark" style="height:40px;margin-top:8px">GET A FREE QUOTE</div>
  </form>
  <p class="abs display" style="left:674px;top:4494px;font-size:20px">PROTECT YOUR ROOF</p>
  <p class="abs display" style="left:672px;top:4530px;font-size:96px;line-height:96px">15% OFF</p>
  <p class="abs display" style="left:674px;top:4630px;font-size:18px">PROTECTION WITH STONECREST BUILDING ROOF SEALANT</p>
  <div class="abs toggle">
    <div class="abs" style="left:0;top:0;width:48px;height:48px;border-radius:50%;background:var(--gold)"></div>
    <div class="abs" style="left:32px;top:0;width:48px;height:48px;border-radius:50%;background:var(--dark)"></div>
  </div>
</section>

<footer>
  <div class="abs" style="left:219px;top:5030px;display:flex;align-items:center;gap:8px"><span style="width:14px;height:14px;border-radius:50%;background:var(--gold)"></span><span style="font-weight:700;font-size:18px;color:#fff;letter-spacing:1px">HALVARD</span></div>
  <div class="abs" style="left:420px;top:4978px">
    <h4 class="f-head" style="margin-bottom:14px">CONTACT INFO</h4>
    <div class="contact-item"><svg width="12" height="14" viewBox="0 0 24 28"><path d="M12 0a10 10 0 0 0-10 10c0 8 10 18 10 18s10-10 10-18A10 10 0 0 0 12 0Zm0 14a4 4 0 1 1 0-8 4 4 0 0 1 0 8Z" fill="#b08f4f"/></svg><span>Some address line goes<br>here city name country</span></div>
    <div class="contact-item"><svg width="12" height="12" viewBox="0 0 24 24"><path d="M5 2h4l2 5-3 2a12 12 0 0 0 7 7l2-3 5 2v4a2 2 0 0 1-2 2C10 21 3 14 3 4a2 2 0 0 1 2-2Z" fill="#b08f4f"/></svg><span>Phone:<br>12-456-7890</span></div>
    <div class="contact-item"><svg width="12" height="12" viewBox="0 0 24 24"><path d="M2 5h20v14H2Zm0 0 10 8 10-8" fill="#b08f4f" stroke="#363b38" stroke-width="1.5"/></svg><span>Email:<br>info@example.com</span></div>
  </div>
  <div class="abs" style="left:703px;top:4978px"><h4 class="f-head" style="margin-bottom:10px">QUICK LINKS</h4><div class="f-list">Home<br>About Us<br>Services<br>Our Projects<br>Latest Blog<br>Contact</div></div>
  <div class="abs" style="left:906px;top:4978px"><h4 class="f-head" style="margin-bottom:10px">COMPANY</h4><div class="f-list">About<br>Reviews<br>Contact</div></div>
  <div class="abs strip"><div>BUILDING</div><div>LANDSCAPING</div><div>DECKING</div><div>MAINTENANCE</div><div>ROOFING</div><div>GUTTERS</div></div>
  <div class="abs social" style="left:132px;top:5319px"></div>
  <div class="abs social" style="left:174px;top:5319px"></div>
  <div class="abs social" style="left:216px;top:5319px"></div>
  <p class="abs" style="left:0;width:1200px;text-align:center;top:5326px;font-size:11px;color:#ddd">© Copyright 2024 All rights reserved</p>
  <div class="abs" style="left:1067px;top:5313px;width:40px;height:40px;border-radius:50%;background:var(--gold)"><svg width="40" height="40" viewBox="0 0 40 40"><path d="M15 23l5-5 5 5" stroke="#fff" stroke-width="2" fill="none"/></svg></div>
</footer>

</body>
</html>
```